Healthcare IT company looking for business card design

We develop IT systems for healthcare that significantly reduces cost and improves quality.

We want a business card design that is professional and clean, and using the colors in our logo.

Doctors and decision makers in the healthcare industry

Healthcare

It should include
Name and title, address, telephone

Torvald Eskberg, CEO
+46 712 480517
torvald@velpamo.se

Serif

0355a3
ed282f

• Clean design
• Professional feel
• N/A
• N/A

```html
<!DOCTYPE html>
<html lang="en">
<head>
<meta charset="utf-8">
<title>Velpamo business card</title>
<link rel="stylesheet" href="https://fonts.googleapis.com/css2?family=Libre+Baskerville:wght@700&family=Nunito+Sans:wght@800&family=Open+Sans:wght@400;600&display=swap">
<style>
  :root {
    --brand-blue: #0355a3;
    --brand-red: #ed282f;
    --card-white: #ffffff;
    --canvas-bg: #e6e7ea;
    --ink-navy: #1a3f8f;
  }
  html, body {
    margin: 0;
    padding: 0;
    width: 1200px;
    height: 900px;
    overflow: hidden;
    background: var(--canvas-bg);
  }
  .canvas {
    position: relative;
    width: 1200px;
    height: 900px;
  }
  .card {
    position: absolute;
    width: 560px;
    height: 320px;
    border-radius: 22px;
    overflow: hidden;
    box-shadow: 0 10px 28px rgba(0,0,0,0.18);
  }
  /* Back side */
  .card-back {
    left: 80px;
    top: 80px;
    background: var(--brand-red);
    display: flex;
    align-items: center;
    justify-content: center;
    gap: 18px;
  }
  .back-dot {
    width: 34px;
    height: 34px;
    border-radius: 50%;
    background: var(--card-white);
  }
  .back-name {
    font-family: "Nunito Sans", sans-serif;
    font-weight: 800;
    font-size: 72px;
    color: var(--card-white);
    letter-spacing: -1px;
  }
  /* Front side */
  .card-front {
    left: 560px;
    top: 500px;
    background: var(--card-white);
  }
  .front-bands {
    position: absolute;
    inset: 0;
  }
  .holder {
    position: absolute;
    left: 30px;
    top: 46px;
  }
  .holder-name {
    font-family: "Libre Baskerville", serif;
    font-weight: 700;
    font-size: 15px;
    color: var(--ink-navy);
    text-transform: uppercase;
    letter-spacing: 0.3px;
  }
  .holder-title {
    font-family: "Open Sans", sans-serif;
    font-size: 12px;
    color: var(--brand-red);
    margin-top: 2px;
  }
  .wordmark {
    position: absolute;
    left: 140px;
    top: 76px;
    font-family: "Nunito Sans", sans-serif;
    font-weight: 800;
    font-size: 88px;
    line-height: 1;
    color: var(--brand-blue);
    letter-spacing: -2px;
  }
  .address {
    position: absolute;
    right: 26px;
    top: 240px;
    text-align: right;
    font-family: "Open Sans", sans-serif;
    font-size: 13px;
    line-height: 1.35;
    color: var(--card-white);
  }
  .contacts {
    position: absolute;
    left: 22px;
    bottom: 10px;
    font-family: "Open Sans", sans-serif;
    font-size: 14px;
    line-height: 1.4;
    color: var(--card-white);
  }
  .contact-row {
    display: flex;
    align-items: center;
    gap: 8px;
  }
  .contact-row svg {
    width: 14px;
    height: 14px;
  }
</style>
</head>
<body>
<main class="canvas">

  <section class="card card-back" aria-label="Card back">
    <span class="back-dot"></span>
    <span class="back-name">Velpamo</span>
  </section>

  <section class="card card-front" aria-label="Card front">
    <svg class="front-bands" viewBox="0 0 560 320" preserveAspectRatio="none" aria-hidden="true">
      <polygon points="300,262 560,165 560,320 300,320" fill="var(--brand-red)"/>
      <polygon points="0,272 330,258 380,320 0,320" fill="var(--brand-blue)"/>
    </svg>

    <div class="holder">
      <div class="holder-name">Torvald Eskberg</div>
      <div class="holder-title">CEO</div>
    </div>

    <div class="wordmark">Velpamo</div>

    <div class="address">
      Palm Street, 21870<br>
      Jeddah, Saudi Arabia
    </div>

    <div class="contacts">
      <div class="contact-row">
        <svg viewBox="0 0 16 16" aria-hidden="true"><path d="M3 2h3l1 4-2 1a9 9 0 0 0 4 4l1-2 4 1v3a1 1 0 0 1-1 1A13 13 0 0 1 2 3a1 1 0 0 1 1-1z" fill="#fff"/></svg>
        <span>+46 712 480517</span>
      </div>
      <div class="contact-row">
        <svg viewBox="0 0 16 16" aria-hidden="true"><rect x="1.5" y="3.5" width="13" height="9" rx="1" fill="none" stroke="#fff" stroke-width="1.4"/><path d="M2 4l6 5 6-5" fill="none" stroke="#fff" stroke-width="1.4"/></svg>
        <span>torvald@velpamo.se</span>
      </div>
    </div>
  </section>

</main>
</body>
</html>
```